Location services company card

Design a new business card for our location services company. I would like to have the front fairly standard with phone and email, logo, name, title etc. Back should feature text: "Location intelligence: make better decisions with maps." I would like either a location pin on the back to make it obvious that we are involved with maps. This could also have a small mud map on the back (use Vensu.com for design inspiration here).

Target Market(s)

Business and government

Industry/Entity Type

Consultant

Contact Information for Business Card

Name, title, address, phone, mobile, email

Font styles to use
Sans Serif

Requirements
Must have
• Flat design with the company colours:
• C60 M0 Y100 K0 and C100 M20 Y0 K65
• Location pin and/or mud map on back.
• Design must be similar/consistent in feel to tqav.com.au

```html
<!DOCTYPE html>
<html lang="en">
<head>
<meta charset="utf-8">
<title>tqav business card</title>
<link rel="stylesheet" href="https://fonts.googleapis.com/css2?family=Oswald:wght@500&family=Poppins:wght@400;500;600&display=swap">
<style>
  :root {
    --page: #e6e1da;
    --card: #f1eee9;
    --navy: #00475a;
    --navy-deep: #0a3f52;
    --green: #66bb2e;
    --ink-light: #e4dccf;
    --ink-soft: #d9cfc0;
  }
  html, body {
    margin: 0;
    padding: 0;
    width: 1200px;
    height: 1047px;
    overflow: hidden;
    background: var(--page);
  }
  .business-card {
    position: absolute;
    left: 150px;
    top: 290px;
    width: 946px;
    height: 514px;
    border-radius: 26px;
    overflow: hidden;
    background: var(--card);
    box-shadow: 0 10px 30px rgba(0,0,0,0.12);
    font-family: "Poppins", sans-serif;
  }
  .band {
    position: absolute;
    left: 0;
    top: 0;
    width: 946px;
    height: 514px;
  }
  .brand {
    position: absolute;
    top: 52px;
    left: 0;
    width: 100%;
    text-align: center;
  }
  .brand-name {
    display: inline-flex;
    align-items: center;
    gap: 16px;
    font-weight: 600;
    font-size: 96px;
    line-height: 1;
    color: var(--navy);
    letter-spacing: -2px;
  }
  .brand-dot {
    width: 24px;
    height: 24px;
    border-radius: 50%;
    background: var(--green);
  }
  .tagline {
    margin-top: 28px;
    font-size: 25px;
    font-weight: 500;
    color: var(--navy);
    letter-spacing: -0.3px;
  }
  .person {
    position: absolute;
    left: 81px;
    top: 378px;
  }
  .person-name {
    font-family: "Oswald", sans-serif;
    font-weight: 500;
    font-size: 48px;
    line-height: 1;
    color: var(--ink-light);
    letter-spacing: 1.5px;
  }
  .person-title {
    margin-top: 10px;
    font-size: 22px;
    color: var(--ink-soft);
  }
  .contact {
    position: absolute;
    left: 460px;
    top: 378px;
    font-size: 20px;
    line-height: 29px;
    color: var(--ink-soft);
    white-space: nowrap;
  }
  .contact p { margin: 0; }
</style>
</head>
<body>
  <div class="business-card">
    <svg class="band" viewBox="0 0 946 514" aria-hidden="true">
      <path d="M0 334 Q473 238 946 342 L946 514 L0 514 Z" fill="var(--green)"/>
      <path d="M0 342 Q473 250 946 350 L946 514 L0 514 Z" fill="var(--navy-deep)"/>
    </svg>

    <div class="brand">
      <div class="brand-name"><span class="brand-dot"></span>tqav</div>
      <div class="tagline">mapping insight for every decision</div>
    </div>

    <div class="person">
      <div class="person-name">DANIEL REYES</div>
      <div class="person-title">Founder</div>
    </div>

    <div class="contact">
      <p>Ph: 555-301-4170 | Mob: 555-301-4170</p>
      <p>info@tqav.com.au</p>
      <p>your address, GPO-123, State, Country.</p>
    </div>
  </div>
</body>
</html>
```